Criação de Papelaria Profissional para Construção & Engenharia
A empresa queria:
" Empresa de 28 anos, muito centrada no nome FALUCENA que é o sobrenome do dono da empresa e maior diferencial no mercado, a experiência! A empresa preza pela qualidade no atendimento ao cliente, sendo que o ponto forte é estar junto ao cliente em todas as etapas do projeto, principalmente durante a obra "

```html
<!DOCTYPE html>
<html lang="pt-BR">
<head>
<meta charset="utf-8">
<title>FALUCENA – Papel Timbrado</title>
<link href="https://fonts.googleapis.com/css2?family=Cinzel:wght@400&family=Lato:wght@400&display=swap" rel="stylesheet">
<style>
  :root {
    --backdrop: #ececec;
    --paper: #ffffff;
    --brand-red: #b3262b;
    --brand-grey: #c9c9c9;
    --ink: #4a4a4a;
    --ink-soft: #7a7a7a;
  }
  html, body {
    margin: 0;
    padding: 0;
    width: 1200px;
    height: 1200px;
    overflow: hidden;
    background: var(--backdrop);
  }
  .letterhead {
    position: absolute;
    left: 211px;
    top: 50px;
    width: 778px;
    height: 1100px;
    background: var(--paper);
    box-shadow: 0 6px 24px rgba(0,0,0,0.12);
  }
  .brand {
    position: absolute;
    top: 92px;
    right: 70px;
    display: flex;
    align-items: center;
    gap: 12px;
  }
  .brand-mark {
    width: 22px;
    height: 22px;
    background: var(--ink);
  }
  .brand-name {
    font-family: "Cinzel", serif;
    font-weight: 400;
    font-size: 34px;
    letter-spacing: 3px;
    color: var(--ink);
  }
  .contact {
    position: absolute;
    left: 56px;
    bottom: 150px;
    font-family: "Lato", sans-serif;
    font-size: 11px;
    line-height: 17px;
    color: var(--ink-soft);
  }
  .contact p { margin: 0; }
  .footer-band {
    position: absolute;
    left: 0;
    bottom: 84px;
    width: 778px;
    height: 16px;
  }
</style>
</head>
<body>
  <main class="letterhead">
    <header class="brand">
      <span class="brand-mark"></span>
      <span class="brand-name">FALUCENA</span>
    </header>

    <address class="contact">
      <p>(81) 3000-0000</p>
      <p>contato@falucena.com.br</p>
      <p>Rua das Obras, 280 - Centro</p>
      <p>Recife - PE - 50000-000</p>
    </address>

    <svg class="footer-band" viewBox="0 0 778 16" aria-hidden="true">
      <polygon points="0,0 214,0 198,16 0,16" fill="var(--brand-red)"/>
      <polygon points="226,0 778,0 778,16 210,16" fill="var(--brand-grey)"/>
    </svg>
  </main>
</body>
</html>
```